Disposable Mini Sauce Pot Design for Asian Chain Food Brands

We operate a Hainan Chicken Rice takeout brand under the name Wokly8, with our official website: www.Wokly8.com.
We offer four signature house sauces and are launching brand-new packaging for our sauce line. We require custom graphic designs exclusively for the sauce cup lids.
Product Material & Base Specs
The sauce cups are made of PP plastic, available in two translucent base options: Translucent White and Translucent Orange.
Four Sauce Varieties for Individual Lid Designs
1. Red Sauce – Fried Sweet Chili Sauce
2.Green Sauce – Scallion Oil Dressing
3.Sweet Soy Sauce
4.Sweet Red Sauce (Special for Fried Chicken)
Differentiate each sauce lid design through unique graphics, typography, or illustrative elements for easy customer identification.
The marking NET WT 2 OZ must be clearly printed on every lid.
**There is no need to print full descriptive text or the full name of the sauces on each lid; the design only needs to clearly differentiate the four sauce varieties.
**Please reference the original design style and brand color palette shown on our official website, and feel free to fully unleash your creativity.
Look and feel
Each slider illustrates characteristics of the customer's brand and the style your logo design should communicate.

```html
<!DOCTYPE html>
<html lang="en">
<head>
<meta charset="utf-8">
<title>Wokly8 Sauce Lids</title>
<link rel="stylesheet" href="https://fonts.googleapis.com/css2?family=Fraunces:opsz,wght@144,900&family=Fredoka:wght@600;700&family=Open+Sans:wght@600&display=swap">
<style>
  :root {
    --bg: #ffffff;
    --cream: #fbf5ea;
    --yellow: #f6c41c;
    --orange-rim: #ef5d25;
    --orange-face: #e2411f;
    --black-rim: #2e2e2b;
    --black-face: #232320;
    --green-rim: #2f9b3f;
    --green-face: #2a6d33;
    --red-rim: #e2222b;
    --red-face: #cf1d26;
  }
  html, body { margin: 0; padding: 0; overflow: hidden; }
  body { width: 1200px; height: 1200px; background: var(--bg); position: relative; }
  .lid-row {
    position: absolute; top: 478px; left: 112px;
    display: flex; gap: 38px;
  }
  .lid {
    width: 215px; height: 244px; border-radius: 28px;
    background: var(--rim); position: relative; box-sizing: border-box;
    padding: 9px;
  }
  .lid-face {
    width: 100%; height: 100%; border-radius: 21px; background: var(--face);
    display: flex; flex-direction: column; align-items: center;
    position: relative; box-sizing: border-box; padding-top: 18px;
  }
  .brand {
    font-family: "Fredoka", sans-serif; font-weight: 700; font-size: 19px;
    color: var(--yellow); line-height: 1; letter-spacing: 0.5px;
  }
  .tag {
    margin-top: 6px; background: var(--cream); color: var(--face);
    font-family: "Fredoka", sans-serif; font-weight: 600; font-size: 10.5px;
    letter-spacing: 0.8px; padding: 1px 14px; border-radius: 8px; line-height: 1.3;
  }
  .name {
    font-family: "Fraunces", serif; font-weight: 900; color: var(--cream);
    text-align: center; line-height: 0.82; letter-spacing: -1.5px;
    margin-top: 4px;
  }
  .name span { display: block; }
  .sub {
    display: flex; align-items: center; gap: 6px; margin-top: 8px;
    font-family: "Fredoka", sans-serif; font-weight: 600; font-size: 15px;
    color: var(--yellow); letter-spacing: 0.8px; line-height: 1;
  }
  .sub svg { width: 11px; height: 16px; }
  .net {
    position: absolute; bottom: -9px; left: 50%; transform: translateX(-50%);
    background: var(--cream); border-radius: 7px 7px 0 0;
    font-family: "Open Sans", sans-serif; font-weight: 600; font-size: 10.5px;
    color: var(--net); width: 88px; text-align: center; padding: 5px 0 4px;
  }
  .lid-sweet-red { --rim: var(--orange-rim); --face: var(--orange-face); --net: var(--orange-face); }
  .lid-sweet-soy { --rim: var(--black-rim); --face: var(--black-face); --net: var(--black-face); }
  .lid-green { --rim: var(--green-rim); --face: var(--green-face); --net: var(--green-face); }
  .lid-red { --rim: var(--red-rim); --face: var(--red-face); --net: var(--red-face); }
</style>
</head>
<body>
<svg width="0" height="0" style="position:absolute">
  <defs>
    <g id="dash-left"><path d="M2 3 L9 5 M1 8 L9 8 M2 13 L9 11" stroke="#f6c41c" stroke-width="2" stroke-linecap="round" fill="none"/></g>
    <g id="dash-right"><path d="M9 3 L2 5 M10 8 L2 8 M9 13 L2 11" stroke="#f6c41c" stroke-width="2" stroke-linecap="round" fill="none"/></g>
  </defs>
</svg>

<main class="lid-row">
  <article class="lid lid-sweet-red">
    <div class="lid-face">
      <div class="brand">Wokly8</div>
      <div class="tag">FRIED CHICKEN</div>
      <div class="name" style="font-size:58px;"><span>sweet</span><span>red</span></div>
      <div class="sub"><svg viewBox="0 0 11 16"><use href="#dash-left"/></svg>SAUCE<svg viewBox="0 0 11 16"><use href="#dash-right"/></svg></div>
      <div class="net">NET WT 2 OZ</div>
    </div>
  </article>

  <article class="lid lid-sweet-soy">
    <div class="lid-face">
      <div class="brand">Wokly8</div>
      <div class="name" style="font-size:62px; margin-top:10px;"><span>sweet</span><span>soy</span></div>
      <div class="sub"><svg viewBox="0 0 11 16"><use href="#dash-left"/></svg>SAUCE<svg viewBox="0 0 11 16"><use href="#dash-right"/></svg></div>
      <div class="net">NET WT 2 OZ</div>
    </div>
  </article>

  <article class="lid lid-green">
    <div class="lid-face">
      <div class="brand">Wokly8</div>
      <div class="name" style="font-size:62px; margin-top:10px;"><span>green</span><span>sauce</span></div>
      <div class="sub"><svg viewBox="0 0 11 16"><use href="#dash-left"/></svg>SCALLION OIL<svg viewBox="0 0 11 16"><use href="#dash-right"/></svg></div>
      <div class="net">NET WT 2 OZ</div>
    </div>
  </article>

  <article class="lid lid-red">
    <div class="lid-face">
      <div class="brand">Wokly8</div>
      <div class="name" style="margin-top:8px;"><span style="font-size:84px;">red</span><span style="font-size:56px;">sauce</span></div>
      <div class="sub"><svg viewBox="0 0 11 16"><use href="#dash-left"/></svg>SWEET CHILI<svg viewBox="0 0 11 16"><use href="#dash-right"/></svg></div>
      <div class="net">NET WT 2 OZ</div>
    </div>
  </article>
</main>
</body>
</html>
```